QV - menu design

Hi,

We require elegant menu design for upscale restaurant. Please find attached the logo and the menu items for your reference.

for inspiration, this is a good website: -
http://www.platewhisper.example/bellfoldnotes/about.php

We are very much open for Menu Size suggestions.

unfortunately the place is going under renovation, we don't have updated images to it. the closest look and feel to our place is http://varnelo.example ..

we are also open for creative options on the shape, the styles, etc. as long as it represents the fine dine feel ...

Thanks ...

Dear All,

We wouldlike to extend our apology for not being able to provide feedbacks on everysingle design. We were extremely busy and we have multiple contests opensimultaneously which makes the process even harder.

However,we would like to thank you all for the efforts you have put into designingour menu. It is very much appreciated …

We wishyou all success in your design ventures and we are quite positive that we willbe working with many of you on many projects in the soon future. 

Thanks & Regards,

TLG Team...

 

 

 

Industry/Entity Type

Restaurant

Requirements
Must have
• Please ensure that there are 'some' images in the menu ... this is very important.
Should not have
• IMPORTANT: -

1. Please DO NOT insert any currency sign to the menu
2. Please keep the prices of the menu at the end of the menu items descriptions NOT beside the menu item names. The font of the price should be similar to the menu item description and please DO NOT bold the numbers. the prices should be subtle.

Thank you ...

```html
<!DOCTYPE html>
<html lang="en">
<head>
<meta charset="utf-8">
<title>QV Cafe – Breakfast Menu</title>
<link href="https://fonts.googleapis.com/css2?family=Questrial&display=swap" rel="stylesheet">
<style>
  :root {
    --backdrop: #000000;
    --paper: #f1f1f1;
    --ink: #262626;
    --ink-soft: #3a3a3a;
    --gold: #a88b66;
    --photo-night-a: #3e4249;
    --photo-night-b: #7c6f5c;
  }
  html, body {
    margin: 0;
    padding: 0;
    width: 1200px;
    height: 1000px;
    overflow: hidden;
    background: var(--backdrop);
    font-family: "Questrial", "Century Gothic", sans-serif;
  }
  .canvas {
    position: relative;
    width: 1200px;
    height: 1000px;
    overflow: hidden;
  }
  .menu-page {
    position: absolute;
    left: 293px;
    top: 35px;
    width: 609px;
    height: 927px;
    background: var(--paper);
    overflow: hidden;
  }
  .page-decor {
    position: absolute;
    inset: 0;
  }
  .menu-title {
    position: absolute;
    margin: 0;
    font-weight: 400;
    white-space: nowrap;
    transform-origin: 0 0;
    line-height: 1;
  }
  .menu-title--the {
    left: 455px;
    top: 98px;
    font-size: 30px;
    letter-spacing: 3px;
    color: var(--gold);
    transform: rotate(-135deg);
  }
  .menu-title--breakfast {
    left: 364px;
    top: 100px;
    font-size: 37px;
    letter-spacing: 5px;
    color: var(--ink);
    transform: rotate(45deg);
  }
  .brand-name {
    position: absolute;
    left: 456px;
    top: 120px;
    font-size: 20px;
    letter-spacing: 5px;
    color: var(--ink);
    white-space: nowrap;
  }
  .menu-item {
    position: absolute;
    width: 205px;
  }
  .menu-item__name {
    margin: 0 0 9px;
    font-size: 15px;
    font-weight: 400;
    letter-spacing: 2.2px;
    color: var(--ink);
    text-transform: uppercase;
  }
  .menu-item__desc {
    margin: 0;
    font-size: 11px;
    line-height: 15.2px;
    color: var(--ink-soft);
  }
</style>
</head>
<body>
<div class="canvas">
  <section class="menu-page">
    <svg class="page-decor" width="609" height="927" viewBox="0 0 609 927">
      <defs>
        <linearGradient id="nightStreet" x1="0" y1="0" x2="1" y2="1">
          <stop offset="0" stop-color="var(--photo-night-b)"/>
          <stop offset="1" stop-color="var(--photo-night-a)"/>
        </linearGradient>
      </defs>
      <!-- top-right diagonal bands -->
      <line x1="170" y1="0" x2="609" y2="439" stroke="var(--ink)" stroke-width="3"/>
      <line x1="186" y1="0" x2="609" y2="423" stroke="var(--ink)" stroke-width="3"/>
      <line x1="207" y1="0" x2="609" y2="402" stroke="var(--gold)" stroke-width="3"/>
      <!-- bottom-left diagonal bands -->
      <line x1="0" y1="697" x2="230" y2="927" stroke="var(--gold)" stroke-width="3"/>
      <line x1="0" y1="718" x2="209" y2="927" stroke="var(--ink)" stroke-width="3"/>
      <line x1="0" y1="736" x2="191" y2="927" stroke="var(--ink)" stroke-width="3"/>
      <!-- photo diamonds -->
      <g role="img" aria-label="Photo of a city avenue at night with tall buildings and car light trails">
        <polygon points="402,228 484,310 402,392 320,310" fill="url(#nightStreet)" stroke="var(--ink)" stroke-width="3"/>
      </g>
      <g role="img" aria-label="Blurred photo of a busy evening street with traffic and headlights">
        <polygon points="162,601 288,727 162,853 36,727" fill="url(#nightStreet)" stroke="var(--gold)" stroke-width="4"/>
      </g>
    </svg>

    <h1 class="menu-title menu-title--the">THE</h1>
    <h1 class="menu-title menu-title--breakfast">BREAKFAST</h1>
    <div class="brand-name">QV CAFE</div>

    <article class="menu-item" style="left:55px; top:122px;">
      <h2 class="menu-item__name">Butter Croissant</h2>
      <p class="menu-item__desc">Served plain with a selection of two jams, a vanilla custard cream, a chocolate Cream and butter curls. 36</p>
    </article>
    <article class="menu-item" style="left:55px; top:233px;">
      <h2 class="menu-item__name">Cheese Croissant</h2>
      <p class="menu-item__desc">Crumbly freshly baked with cheese filling. 29</p>
    </article>
    <article class="menu-item" style="left:55px; top:328px;">
      <h2 class="menu-item__name">Daily Fresh Eggs</h2>
      <p class="menu-item__desc">A choice of poached, scrambled, pan fried, omelet) all served with toasted Bread, mushrooms, roasted tomatoes and chicken sausages. 59</p>
    </article>
    <article class="menu-item" style="left:55px; top:454px;">
      <h2 class="menu-item__name">Healthy Time</h2>
      <p class="menu-item__desc">One choice of hot beverage from our cafe served with fruit salad, natural Yoghurt, whole wheat bread vegetable sandwiches and sugar free biscuits selection.49</p>
    </article>

    <article class="menu-item" style="left:355px; top:443px;">
      <h2 class="menu-item__name">Energy Time</h2>
      <p class="menu-item__desc">One choice of hot beverage from our cafe served with finger chocolate muffins,<br>Poached egg with toasted bread and crispy beef bacon, crepe roll with goat Cheese and honey and finger chocolate cream with salted cookies. 59</p>
    </article>
    <article class="menu-item" style="left:355px; top:610px;">
      <h2 class="menu-item__name">QV Time</h2>
      <p class="menu-item__desc">One choice of hot beverage from our cafe served with our selection of scones, Smoked salmon and avocado sandwich, roasted sausages sandwich, grilled vegetables sandwich, selection of our best biscuits. 59</p>
    </article>
    <article class="menu-item" style="left:355px; top:746px;">
      <h2 class="menu-item__name">The Arabic Breakfast</h2>
      <p class="menu-item__desc">Choice of Zattar Manakish and Cheese Manakish, served with one choice of hot beverage from our cafe and fresh orange juice. 59</p>
    </article>
  </section>
</div>
</body>
</html>
```